Design the Mobile Version of Existing Web Based Health Platform

Nuvorel is a social business enterprise that focus on public health by applying innovative healthcare services and consumer internet technology. Nuvorel offers a personalized platform of health promotion and disease prevention that puts the individual back in control of his life.

Nuvorel is looking for a Mobile Web UX/Visual Design professional to create a mobile version of Nuvorel website platform for iPhone, iPad/tablet and Android.

Contestants must to check www.nuvorel-saude.com.br to have a better understanding of Nuvorel Platform by creating an account (it's in portuguese, but anyone can get the general idea).

The mobile version of Nuvorel should have very similar functionality and user flows. This job is not to reengineer or re-imagine Nuvorel. It is just to reformat the existing functionality so it works well on mobile devices.

This description below is to help you to understand the core features of the platform (check the attachments to see the new web design of each one):

- Personally Controlled Health Record - PCHR enables an individual to own and manage a complete, secure, digital copy of her health and wellness information.
- Health Risk Assessments - is a process to estimate the nature and probability of adverse health effects, based on personal and family historical data, behavior and environment.
- Simulation of future health - "what if analysis" that emphasizes health education and behavior change.
- Daily Challenges - a program that gives you the opportunity to the participant to advance his personal well-being by doing simple daily challenges
- Health Alerts and Recommendations and Missing Data - Recommendations based on Health Ministry Guidelines and National Wellness Review Board (NWRB), plus notifications to update outdated information.

The deliverable for this project is a psd file with a designed mobile version of Nuvorel.

A new design of the web platform is under construction. You can also check it looking at the files attached.

Target Market(s)

people 25-40 years old, 60% female, socially engaged

Industry/Entity Type

Healthcare

Requirements
Must have
• iPhone, iPad and Android version

Design must cover all current functionalities available on the web version (please, ensure you understand all features by creating an account at www.nuvorel-saude.com.br)

- Login/Sign up
- Welcome (first assessment)
- Add to Personal Controlled Health Record (PCHR)
- Update/Remove PCHR
- List PCHR
- Bodyscope (risk assessmen results)
- Simulation
- Alerts
- Missing data
- Recommendations
- StepQuest
- Badges
- Configurations

It's important to check the attachments to see how the web platform design is evolving.

```html
<!DOCTYPE html>
<html lang="pt-BR">
<head>
<meta charset="utf-8">
<title>Nuvorel – Sign up</title>
<link rel="stylesheet" href="https://fonts.googleapis.com/css2?family=Arimo:wght@400;700&family=Roboto+Condensed:wght@700&display=swap">
<style>
  :root {
    --canvas-bg: #ececec;
    --screen-bg-top: #f6f4f1;
    --screen-bg-bottom: #eeeae6;
    --card-bg: #ffffff;
    --card-border: #d9d9d9;
    --brand-green: #8dc63f;
    --text-grey: #8c8c8c;
    --field-border: #cfcfcf;
    --field-text: #8a8a8a;
    --square-blue: #3b5998;
    --link-blue: #2c4a8c;
    --body-text: #555555;
  }
  * { box-sizing: border-box; margin: 0; padding: 0; }
  html, body {
    width: 1200px; height: 800px; overflow: hidden;
    background: var(--canvas-bg);
    font-family: "Arimo", Arial, sans-serif;
  }
  .screen {
    position: absolute; left: 390px; top: 35px;
    width: 420px; height: 730px; overflow: hidden;
  }
  .screen-pattern {
    position: absolute; inset: 0;
    background: linear-gradient(180deg, var(--screen-bg-top), var(--screen-bg-bottom));
  }
  .signup-card {
    position: absolute; left: 30px; top: 52px;
    width: 355px; height: 636px;
    background: var(--card-bg);
    border: 1px solid var(--card-border);
    border-radius: 8px;
    box-shadow: 0 1px 4px rgba(0,0,0,0.08);
  }
  .hero-illustration {
    position: absolute; left: 53px; top: 21px;
    width: 248px; height: 248px; border-radius: 50%;
    background: radial-gradient(circle at 50% 45%, #b9bcbf 0%, #c9ccce 45%, #e7b9a8 75%, #cfe3b1 100%);
  }
  .brand-name {
    position: absolute; left: 0; right: 0; top: 284px;
    text-align: center; font-weight: 700; font-size: 36px;
    color: var(--brand-green); letter-spacing: -0.5px;
  }
  .brand-tagline {
    position: absolute; left: 0; right: 0; top: 330px;
    text-align: center; font-weight: 700; font-size: 19px; line-height: 26px;
    color: var(--text-grey);
  }
  .field {
    position: absolute; left: 37px; width: 280px; height: 38px;
    border: 1px solid var(--field-border); border-radius: 2px;
    background: #fff; padding: 0 12px;
    font-family: "Arimo", Arial, sans-serif; font-size: 14px;
    color: var(--field-text); display: flex; align-items: center;
  }
  .field-email { top: 390px; }
  .field-password { top: 450px; }
  .field-retype { top: 505px; }
  .signup-button {
    position: absolute; left: 37px; top: 560px;
    width: 280px; height: 38px; display: flex; align-items: stretch;
    background: var(--brand-green); border-radius: 2px; overflow: hidden;
  }
  .signup-button .mark {
    width: 38px; flex: none; background: var(--square-blue);
  }
  .signup-button .label {
    flex: 1; display: flex; align-items: center; justify-content: center;
    font-family: "Roboto Condensed", "Arial Narrow", sans-serif;
    font-weight: 700; font-size: 18px; color: #fff; letter-spacing: 0.2px;
  }
  .terms {
    position: absolute; left: 0; right: 0; top: 608px;
    display: flex; justify-content: center; align-items: center; gap: 6px;
    font-size: 11px; color: var(--body-text);
  }
  .terms .checkbox {
    width: 10px; height: 10px; border: 1px solid #bdbdbd; background: #fff;
  }
  .terms .link { color: var(--link-blue); }
</style>
</head>
<body>
  <main class="screen">
    <div class="screen-pattern" role="img" aria-label="Faint pattern of health and sport icons: bicycles, balls, stopwatches, fruit, dumbbells"></div>
    <section class="signup-card">
      <div class="hero-illustration" role="img" aria-label="Circular cluster of colourful health icons: fruit, sports balls, bicycle, stopwatches, sneaker, fish, dumbbell, scale, tape measure"></div>
      <h1 class="brand-name">Nuvorel</h1>
      <p class="brand-tagline">Plataforma de Saúde<br>Pessoal</p>
      <div class="field field-email">Email address...</div>
      <div class="field field-password">Password...</div>
      <div class="field field-retype">Retype Password...</div>
      <div class="signup-button">
        <span class="mark"></span>
        <span class="label">SIGN UP WITH LINKORA</span>
      </div>
      <p class="terms"><span class="checkbox"></span><span>I accept the <span class="link">Terms and Conditions</span></span></p>
    </section>
  </main>
</body>
</html>
```